Business card design for Automotive workshop

We need a business card for a new automotive repair and tyre shop called Ridgeback Prime Automotive located in New Zealand. We are a clean, modern and fresh workshop and company.

Front needs to feature logo,
my name:
Lachie Westergaard (director)

Address:
48 Marlow Lane
Tarawai 3582

Phone: 07 842 1937
Mobile: 027 519 2764
Email: office@ridgebackmotors.co.nz
Website: ridgebackmotors.co.nz

Back needs to feature an area to write down appointment details, date and time.

Also feature a list of jobs and work we do such as,
Vehicle Servicing
All Mechanical Repairs
Warrant of Fitness
Tyres & Wheel Alignments
Automotive Diagnostics
Automotive Parts & Supplies

```html
<!DOCTYPE html>
<html lang="en">
<head>
<meta charset="utf-8">
<title>Ridgeback Prime Automotive – Business Card</title>
<link href="https://fonts.googleapis.com/css2?family=Poppins:wght@400;500;600;700;800&display=swap" rel="stylesheet">
<style>
  :root {
    --bg: #2b2b2d;
    --card: #0b0b0c;
    --red: #e3232b;
    --white: #ffffff;
    --field: #ffffff;
    --ink: #111111;
  }
  * { box-sizing: border-box; margin: 0; padding: 0; }
  html, body { width: 1200px; height: 880px; overflow: hidden; }
  body {
    background: var(--bg);
    font-family: "Poppins", sans-serif;
    color: var(--white);
    position: relative;
  }
  .card {
    position: absolute;
    left: 250px;
    width: 700px;
    height: 400px;
    background: var(--card);
    border-radius: 4px;
    overflow: hidden;
    box-shadow: 0 18px 40px rgba(0,0,0,.45);
  }
  .card--back { top: 20px; }
  .card--front { top: 460px; }

  /* Brand name */
  .brand {
    position: absolute;
    display: flex;
    align-items: center;
    gap: 12px;
    color: var(--white);
    font-weight: 700;
    text-transform: uppercase;
    line-height: 1.05;
  }
  .brand__dot { background: var(--red); flex: none; }
  .card--back .brand { left: 250px; top: 34px; font-size: 26px; }
  .card--back .brand__dot { width: 16px; height: 16px; }
  .card--front .brand { left: 60px; top: 60px; font-size: 38px; }
  .card--front .brand__dot { width: 22px; height: 22px; }
  .brand__sub { display: block; font-size: .52em; letter-spacing: .22em; }

  /* Services list */
  .services {
    position: absolute;
    left: 46px;
    top: 110px;
    list-style: none;
  }
  .services li {
    display: flex;
    align-items: center;
    gap: 14px;
    font-size: 16px;
    font-weight: 500;
    text-transform: uppercase;
    line-height: 1.4;
    margin-bottom: 10px;
  }
  .services li::before {
    content: "";
    width: 11px; height: 11px;
    border-radius: 50%;
    border: 3px solid var(--red);
    flex: none;
  }

  /* Appointment fields */
  .appointment { position: absolute; right: 40px; top: 112px; width: 330px; }
  .appointment__row { display: flex; align-items: center; gap: 10px; margin-bottom: 22px; }
  .appointment__label { color: var(--red); font-size: 17px; font-weight: 600; width: 58px; }
  .appointment__field {
    flex: 1;
    height: 42px;
    background: var(--field);
    border-radius: 8px;
    color: var(--ink);
    display: flex;
    align-items: center;
    justify-content: space-around;
    font-size: 18px;
    font-weight: 500;
    padding: 0 12px;
  }
  .appointment__field small { font-size: 12px; margin-left: auto; }

  .web-band {
    position: absolute;
    left: 0; right: 0; bottom: 0;
    height: 60px;
    background: var(--red);
    display: flex;
    align-items: center;
    justify-content: center;
    font-size: 22px;
    font-weight: 800;
    letter-spacing: .02em;
    text-transform: uppercase;
  }

  /* Front */
  .rule-red { position: absolute; right: 40px; top: 42px; width: 170px; height: 2px; background: var(--red); }
  .address { position: absolute; right: 40px; top: 66px; font-size: 16px; line-height: 1.45; width: 170px; }
  .rule-white { position: absolute; left: 340px; top: 160px; width: 250px; height: 1.5px; background: var(--white); }

  .person { position: absolute; left: 60px; top: 178px; }
  .person__name { color: var(--red); font-size: 26px; font-weight: 800; text-transform: uppercase; letter-spacing: .01em; line-height: 1.1; }
  .person__role { font-size: 16px; font-weight: 700; text-transform: uppercase; }

  .contacts { position: absolute; left: 60px; top: 252px; list-style: none; }
  .contacts li { display: flex; align-items: center; gap: 12px; font-size: 16px; line-height: 1; margin-bottom: 10px; }
  .contacts svg { width: 15px; height: 15px; fill: var(--red); flex: none; }

  .front-band { position: absolute; left: 0; bottom: 0; width: 700px; height: 60px; }
</style>
</head>
<body>

<section class="card card--back" aria-label="Card back">
  <div class="brand">
    <span class="brand__dot"></span>
    <span>Ridgeback Prime<span class="brand__sub">Automotive</span></span>
  </div>

  <ul class="services">
    <li>Vehicle Servicing</li>
    <li>All Mechanical Repairs</li>
    <li>Warrant of Fitness</li>
    <li>Tyres &amp; Wheel Alignments</li>
    <li>Automotive Diagnostics</li>
    <li>Automotive Parts &amp; Supplies</li>
  </ul>

  <div class="appointment">
    <div class="appointment__row">
      <span class="appointment__label">Date:</span>
      <span class="appointment__field"><span>/</span><span>/</span></span>
    </div>
    <div class="appointment__row">
      <span class="appointment__label">Time:</span>
      <span class="appointment__field"><span>:</span><small>AM / PM</small></span>
    </div>
  </div>

  <div class="web-band">www.ridgebackmotors.co.nz</div>
</section>

<section class="card card--front" aria-label="Card front">
  <div class="brand">
    <span class="brand__dot"></span>
    <span>Ridgeback Prime<span class="brand__sub">Automotive</span></span>
  </div>

  <div class="rule-red"></div>
  <p class="address">48 Marlow Lane<br>Tarawai 3582</p>
  <div class="rule-white"></div>

  <div class="person">
    <p class="person__name">Lachie Westergaard</p>
    <p class="person__role">Owner</p>
  </div>

  <ul class="contacts">
    <li><svg viewBox="0 0 24 24"><path d="M6.6 10.8a15 15 0 0 0 6.6 6.6l2.2-2.2a1 1 0 0 1 1-.25 11.4 11.4 0 0 0 3.6.57 1 1 0 0 1 1 1V20a1 1 0 0 1-1 1A17 17 0 0 1 3 4a1 1 0 0 1 1-1h3.5a1 1 0 0 1 1 1c0 1.250.2 2.450.57 3.57a1 1 0 0 1-.25 1z"/></svg>07 842 1937</li>
    <li><svg viewBox="0 0 24 24"><path d="M7 1h10a2 2 0 0 1 2 2v18a2 2 0 0 1-2 2H7a2 2 0 0 1-2-2V3a2 2 0 0 1 2-2zm0 3v14h10V4z"/></svg>027 519 2764</li>
    <li><svg viewBox="0 0 24 24"><path d="M2 5h20v14H2zm2 2v.5l8 5 8-5V7l-8 5z"/></svg>office@ridgebackmotors.co.nz</li>
    <li><svg viewBox="0 0 24 24"><path d="M12 2a10 10 0 1 0 0 20 10 10 0 0 0 0-20zm6.9 6h-3a15 15 0 0 0-1.3-3.9A8 8 0 0 1 18.9 8zM12 4c.8 1.2 1.5 2.5 1.9 4h-3.8c.4-1.5 1.1-2.8 1.9-4zM4.3 14a8 8 0 0 1 0-4h3.4a16 16 0 0 0 0 4zm.8 2h3a15 15 0 0 0 1.3 3.9A8 8 0 0 1 5.1 16zm3-8h-3a8 8 0 0 1 4.3-3.9A15 15 0 0 0 8.1 8zM12 20c-.8-1.2-1.5-2.5-1.9-4h3.8c-.4 1.5-1.1 2.8-1.9 4zm2.3-6H9.7a14 14 0 0 1 0-4h4.6a14 14 0 0 1 0 4zm.3 5.9a15 15 0 0 0 1.3-3.9h3a8 8 0 0 1-4.3 3.9zm1.7-5.9a16 16 0 0 0 0-4h3.4a8 8 0 0 1 0 4z"/></svg>ridgebackmotors.co.nz</li>
  </ul>

  <svg class="front-band" viewBox="0 0 700 60" preserveAspectRatio="none" aria-hidden="true">
    <path d="M0 46 L520 46 C540 46 540 30 560 30 L700 30 L700 60 L0 60 Z" fill="var(--red)"/>
  </svg>
</section>

</body>
</html>
```